Business Card Ayurvedic Massage

I'm starting with my ayurvedic massage business and need a business card design. The design should be inline with my brand/logo as well as with the design of my website (www.lumo-thara.ch).
Front: logo and text "Ayurvedische Massagen"
back: name and adress (see details https://www.lumo-thara.ch/kontakt.html)

```html
<!DOCTYPE html>
<html lang="de">
<head>
<meta charset="utf-8">
<title>lumo-thara – Business Card</title>
<link href="https://fonts.googleapis.com/css2?family=Roboto+Condensed:wght@400;700&family=Arimo&display=swap" rel="stylesheet">
<style>
  :root {
    --stage: #000000;
    --paper: #ffffff;
    --gold-deep: #cc960c;
    --gold-mid: #e6b91e;
    --gold-light: #f6e7a0;
    --gold-line: #d49d0a;
    --maroon: #7a1d12;
    --ink: #111111;
  }
  html, body {
    margin: 0;
    padding: 0;
    width: 1200px;
    height: 1200px;
    overflow: hidden;
    background: var(--stage);
  }
  .canvas {
    position: relative;
    width: 1200px;
    height: 1200px;
    background: var(--stage);
  }
  .card {
    position: absolute;
    left: 232px;
    width: 736px;
    height: 420px;
    display: block;
  }
  .card--front { top: 134px; }
  .card--back { top: 646px; }
  .brand-name {
    font-family: "Roboto Condensed", sans-serif;
    font-weight: 700;
    font-size: 42px;
    fill: var(--maroon);
  }
  .holder-name {
    font-family: "Arimo", sans-serif;
    font-size: 35px;
    fill: var(--gold-line);
  }
  .contact-text {
    font-family: "Roboto Condensed", sans-serif;
    font-size: 23px;
    fill: var(--ink);
  }
  .web-text {
    font-family: "Roboto Condensed", sans-serif;
    font-size: 31px;
    fill: var(--ink);
  }
</style>
</head>
<body>
<div class="canvas">

  <!-- Front side -->
  <svg class="card card--front" viewBox="0 0 736 420" xmlns="http://www.w3.org/2000/svg">
    <defs>
      <linearGradient id="goldTopLeft" x1="0" y1="0" x2="1" y2="0">
        <stop offset="0" stop-color="#cf950a"/>
        <stop offset="0.55" stop-color="#e6c050"/>
        <stop offset="1" stop-color="#f8eba8"/>
      </linearGradient>
      <linearGradient id="goldBottomRight" x1="0" y1="0" x2="1" y2="0">
        <stop offset="0" stop-color="#f1c93a"/>
        <stop offset="0.5" stop-color="#f5d43c"/>
        <stop offset="1" stop-color="#cc9a10"/>
      </linearGradient>
      <linearGradient id="elephantTone" x1="0" y1="0" x2="0" y2="1">
        <stop offset="0" stop-color="#e8a81c"/>
        <stop offset="0.5" stop-color="#b44a1a"/>
        <stop offset="1" stop-color="#d9961a"/>
      </linearGradient>
    </defs>
    <rect class="card-paper" width="736" height="420" fill="var(--paper)"/>
    <polygon class="corner-band" points="0,0 246,0 0,197" fill="url(#goldTopLeft)"/>
    <polygon class="corner-band" points="736,223 736,420 490,420" fill="url(#goldBottomRight)"/>
    <rect role="img" aria-label="Illustration: decorated ceremonial elephant with parasol, facing right" x="100" y="120" width="140" height="182" rx="14" fill="url(#elephantTone)"/>
    <rect role="img" aria-label="Illustration: decorated ceremonial elephant with parasol, facing left" x="494" y="120" width="140" height="182" rx="14" fill="url(#elephantTone)"/>
    <text class="brand-name" x="368" y="244" text-anchor="middle">lumo-thara</text>
  </svg>

  <!-- Back side -->
  <svg class="card card--back" viewBox="0 0 736 420" xmlns="http://www.w3.org/2000/svg">
    <defs>
      <linearGradient id="goldFooter" x1="0" y1="0" x2="1" y2="0">
        <stop offset="0" stop-color="#cf950a"/>
        <stop offset="0.25" stop-color="#f6e7a0"/>
        <stop offset="0.6" stop-color="#f2be14"/>
        <stop offset="0.88" stop-color="#f3e6a2"/>
        <stop offset="1" stop-color="#cf9a10"/>
      </linearGradient>
      <linearGradient id="elephantToneBack" x1="0" y1="0" x2="0" y2="1">
        <stop offset="0" stop-color="#e8a81c"/>
        <stop offset="0.5" stop-color="#b44a1a"/>
        <stop offset="1" stop-color="#d9961a"/>
      </linearGradient>
    </defs>
    <rect class="card-paper" width="736" height="420" fill="var(--paper)"/>

    <rect role="img" aria-label="Illustration: decorated ceremonial elephant with parasol, facing right" x="100" y="16" width="140" height="184" rx="14" fill="url(#elephantToneBack)"/>
    <rect role="img" aria-label="Illustration: decorated ceremonial elephant with parasol, facing left" x="494" y="16" width="140" height="184" rx="14" fill="url(#elephantToneBack)"/>
    <text class="brand-name" x="368" y="140" text-anchor="middle">lumo-thara</text>

    <rect class="divider" x="28" y="207" width="680" height="5" fill="var(--gold-line)"/>
    <text class="holder-name" x="702" y="248" text-anchor="end">YOUR NAME</text>
    <rect class="name-underline" x="488" y="253" width="220" height="2.5" fill="var(--gold-line)"/>

    <!-- pin icon -->
    <g class="icon-pin" transform="translate(38 322)">
      <path d="M0,-14 a9,9 0 0 1 9,9 c0,7 -9,17 -9,17 c0,0 -9,-10 -9,-17 a9,9 0 0 1 9,-9 z" fill="var(--gold-mid)"/>
      <circle cx="0" cy="-5" r="4" fill="var(--paper)"/>
    </g>
    <text class="contact-text" x="66" y="315">Mira Berchtold, lumo-thara,</text>
    <text class="contact-text" x="66" y="340">Lindenweg 14, 8853 Lachen (SZ)</text>

    <!-- mail icon -->
    <g class="icon-mail" transform="translate(490 306)">
      <rect width="29" height="18" fill="var(--gold-mid)"/>
      <polyline points="0,0 14.5,10 29,0" fill="none" stroke="var(--paper)" stroke-width="1.6"/>
    </g>
    <text class="contact-text" x="528" y="323">info@lumo-thara.ch</text>

    <!-- phone icon -->
    <g class="icon-phone" transform="translate(505 357)">
      <circle r="12" fill="var(--gold-mid)"/>
      <path d="M-5,-6 c-2,4 2,11 8,12 l2,-3 l-3,-2 l-1.5,1.5 c-2,-1 -4,-3 -4.5,-5 l1.5,-1.5 l-2,-3 z" fill="var(--paper)"/>
    </g>
    <text class="contact-text" x="530" y="366">+41 77 000 12 34</text>

    <!-- footer band -->
    <polygon class="footer-band" points="0,370 300,370 330,394 736,394 736,420 0,420" fill="url(#goldFooter)"/>
    <polygon class="footer-stripe" points="326,378 736,378 736,385 334,385" fill="var(--ink)"/>
    <text class="web-text" x="52" y="407">www.lumo-thara.ch</text>
  </svg>

</div>
</body>
</html>
```